Kestrel Bridge Consulting (KBC) Business Card Design

I would like to create double-sided business cards that contain:
1) Name: Derek Molvane
2) Phone Number: +1 (555) 218-4907
3) Email: Derek.Molvane@KestrelBridgeConsulting.example
4) Website: KestrelBridgeConsulting.example

I would like to include my logo and a color scheme similar to the Varnholt Grand Prix Ostera squad color scheme (black, silver, greenish-blue – but can also include regular blue)

What we do: Our company develops and delivers innovative and pragmatic information technology and cybersecurity risk and compliance solutions for organizations in the commercial market as well as the federal, and state/local sectors.

```html
<!DOCTYPE html>
<html lang="en">
<head>
<meta charset="utf-8">
<title>Kestrel Bridge Consulting — Business Card</title>
<link href="https://fonts.googleapis.com/css2?family=Montserrat:wght@400;600;700&display=swap" rel="stylesheet">
<style>
  :root {
    --backdrop: #b3b3b3;
    --card: #424695;
    --silver: #c8c8cc;
    --charcoal: #26262b;
    --teal: #1fc7bd;
    --white: #ffffff;
    --lavender: #a9abd3;
    --icon: #c9cbe6;
  }
  * { box-sizing: border-box; margin: 0; padding: 0; }
  html, body {
    width: 1154px; height: 1200px; overflow: hidden;
    background: var(--backdrop);
    font-family: "Montserrat", sans-serif;
  }
  .canvas { position: relative; width: 1154px; height: 1200px; }
  .card {
    position: absolute;
    background: var(--card);
    border-radius: 30px;
    box-shadow: 0 6px 10px rgba(0,0,0,0.18);
    overflow: hidden;
  }
  .card--front { left: 203px; top: 147px; width: 753px; height: 430px; }
  .card--back  { left: 204px; top: 621px; width: 770px; height: 440px; }

  .brand-mark { position: absolute; border-radius: 50%; }
  .card--front .brand-mark { left: 120px; top: 150px; width: 150px; height: 150px; background: var(--charcoal); }
  .card--back .brand-mark { left: 169px; top: 43px; width: 120px; height: 120px; background: var(--teal); }

  .brand-name {
    position: absolute;
    font-weight: 600;
    text-transform: uppercase;
    letter-spacing: 1px;
  }
  .card--front .brand-name { left: 307px; top: 165px; font-size: 35px; line-height: 38px; color: var(--silver); }
  .card--back .brand-name { left: 322px; top: 55px; font-size: 30px; line-height: 33px; color: var(--white); }

  .name-accent { position: absolute; left: 0; top: 226px; width: 15px; height: 63px; background: var(--lavender); }
  .person-name { position: absolute; left: 44px; top: 214px; font-size: 31px; font-weight: 700; color: var(--lavender); }
  .person-title { position: absolute; left: 42px; top: 260px; font-size: 20.5px; font-weight: 400; color: var(--white); letter-spacing: 0.3px; }
  .divider { position: absolute; left: 38px; top: 297px; width: 690px; height: 2px; background: var(--white); }

  .contact-list { position: absolute; left: 43px; top: 320px; list-style: none; }
  .contact-item {
    display: flex; align-items: center; gap: 12px;
    height: 30px; margin-bottom: 0;
    font-size: 19.5px; color: var(--white);
  }
  .contact-item svg { width: 18px; height: 18px; flex: none; }
</style>
</head>
<body>
<div class="canvas">

  <section class="card card--front" aria-label="Card front">
    <span class="brand-mark"></span>
    <div class="brand-name">Kestrel<br>Bridge<br>Consulting</div>
  </section>

  <section class="card card--back" aria-label="Card back">
    <span class="brand-mark"></span>
    <div class="brand-name">Kestrel<br>Bridge<br>Consulting</div>

    <span class="name-accent"></span>
    <h1 class="person-name">Derek Molvane</h1>
    <p class="person-title">MANAGING DIRECTOR</p>
    <span class="divider"></span>

    <ul class="contact-list">
      <li class="contact-item">
        <svg viewBox="0 0 24 24" fill="none" stroke="var(--icon)" stroke-width="2" stroke-linecap="round" stroke-linejoin="round"><path d="M22 16.9v3a2 2 0 0 1-2.2 2 19.8 19.8 0 0 1-8.6-3.1 19.5 19.5 0 0 1-6-6A19.8 19.8 0 0 1 2.1 4.2 2 2 0 0 1 4.1 2h3a2 2 0 0 1 2 1.7c.1 1 .4 1.9.7 2.8a2 2 0 0 1-.5 2.1L8 9.8a16 16 0 0 0 6 6l1.3-1.3a2 2 0 0 1 2.1-.4c.9.3 1.8.6 2.8.7a2 2 0 0 1 1.8 2z"/></svg>
        <span>+1 (555) 218-4907</span>
      </li>
      <li class="contact-item">
        <svg viewBox="0 0 24 24" fill="var(--icon)"><path d="M2 5h20v14H2z"/><path d="M2 5l10 8 10-8" fill="none" stroke="var(--card)" stroke-width="2"/></svg>
        <span>Derek.Molvane@KestrelBridgeConsulting.example</span>
      </li>
      <li class="contact-item">
        <svg viewBox="0 0 24 24" fill="none" stroke="var(--icon)" stroke-width="2"><circle cx="12" cy="12" r="10"/><path d="M2 12h20M12 2a15 15 0 0 1 0 20M12 2a15 15 0 0 0 0 20"/></svg>
        <span>KestrelBridgeConsulting.example</span>
      </li>
    </ul>
  </section>

</div>
</body>
</html>
```